brownie sticker

i need a sticker to wrap around a clear rectangle box that will contain chocolate brownies. the sticker must be 17cm x 7 cm.
the sticker will be placed in the folowing direction.
7cm of the sticker on front of box, 3cm for each side of the box, and 4 cm on the bottom to seal the box closed.
I HAVE ATTACHED A VERY ROUGH PICTURE FOR YOU TO SEE POSITION AND DIRECTION OF STICKER.

Target Market(s)

our product will be mainly seen in upmarket grocery stores and farmers markets.

Requirements
Must have
• IT MUST CONTAIN THE FOLLOWING IN SMALL PRINT at the bottom of the sticker...
produced by marigolds bakehouse
48 kellow st
cheltenham
vic 3274
ph: 047658913
email: marigoldsbakehouse@mailbrook.net

```html
<!DOCTYPE html>
<html lang="en">
<head>
<meta charset="utf-8">
<title>Marigolds Bakehouse – Box Sticker</title>
<link href="https://fonts.googleapis.com/css2?family=Alegreya+Sans:wght@400;500;700&display=swap" rel="stylesheet">
<style>
  :root {
    --cocoa: #5a2d1b;
    --caramel: #c49a6c;
    --ink: #111111;
    --paper: #ffffff;
  }
  html, body {
    margin: 0;
    padding: 0;
    overflow: hidden;
    background: var(--paper);
  }
  .sticker {
    position: relative;
    width: 1200px;
    height: 494px;
    overflow: hidden;
    background: var(--paper);
    font-family: "Alegreya Sans", "Trebuchet MS", sans-serif;
  }
  .foliage {
    position: absolute;
    display: block;
  }
  .foliage--top-left {
    left: 0;
    top: 0;
    width: 382px;
    height: 227px;
  }
  .foliage--bottom-right {
    right: 0;
    bottom: 0;
    width: 340px;
    height: 234px;
  }
  .brand__dot {
    position: absolute;
    left: 602px;
    top: 50px;
    width: 30px;
    height: 30px;
    border-radius: 50%;
    background: var(--cocoa);
  }
  .brand__name {
    position: absolute;
    left: 317px;
    top: 136px;
    width: 600px;
    margin: 0;
    color: var(--cocoa);
    font-size: 60px;
    line-height: 60px;
    font-weight: 500;
    letter-spacing: 3px;
    text-align: center;
    text-transform: uppercase;
  }
  .brand__sub {
    position: absolute;
    left: 317px;
    top: 194px;
    width: 600px;
    padding-left: 12px;
    box-sizing: border-box;
    color: var(--cocoa);
    font-size: 26px;
    line-height: 26px;
    font-weight: 500;
    letter-spacing: 12px;
    text-align: center;
    text-transform: uppercase;
  }
  .about {
    position: absolute;
    left: 347px;
    top: 247px;
    width: 540px;
    margin: 0;
    color: var(--caramel);
    font-size: 18px;
    line-height: 27px;
    text-align: center;
  }
  .contact {
    position: absolute;
    left: 367px;
    top: 422px;
    width: 500px;
    margin: 0;
    color: var(--cocoa);
    font-size: 21px;
    line-height: 24px;
    font-weight: 700;
    text-align: center;
  }
  .imprint {
    position: absolute;
    left: 387px;
    top: 456px;
    width: 460px;
    margin: 0;
    color: var(--cocoa);
    font-size: 11px;
    line-height: 14px;
    text-align: center;
  }
  .ingredients {
    position: absolute;
    left: 891px;
    top: 84px;
    margin: 0;
    color: var(--cocoa);
    font-size: 21px;
    line-height: 24px;
    font-weight: 700;
    letter-spacing: 0.5px;
    writing-mode: vertical-rl;
    transform: rotate(180deg);
  }
  .barcode-area {
    position: absolute;
    left: 1050px;
    top: 37px;
    width: 113px;
    height: 262px;
    box-sizing: border-box;
    border: 2px solid var(--ink);
    background: var(--paper);
    display: flex;
    align-items: center;
    justify-content: center;
  }
  .barcode-area__label {
    color: var(--cocoa);
    font-size: 19px;
    font-weight: 700;
    letter-spacing: 0.5px;
    writing-mode: vertical-rl;
    transform: rotate(180deg);
  }
</style>
</head>
<body>
  <main class="sticker">
    <svg class="foliage foliage--top-left" role="img" aria-label="Decorative leaf illustration in caramel and cocoa tones" viewBox="0 0 382 227">
      <defs>
        <linearGradient id="foliage-top" x1="0" y1="0" x2="1" y2="0">
          <stop offset="0" stop-color="#c49a6c"/>
          <stop offset="0.4" stop-color="#c49a6c"/>
          <stop offset="0.6" stop-color="#5a2d1b"/>
          <stop offset="1" stop-color="#5a2d1b"/>
        </linearGradient>
      </defs>
      <path d="M0 0 H382 V150 Q382 227 305 227 H0 Z" fill="url(#foliage-top)" opacity="0.9"/>
    </svg>

    <svg class="foliage foliage--bottom-right" role="img" aria-label="Decorative leaf illustration in caramel and cocoa tones" viewBox="0 0 340 234">
      <defs>
        <linearGradient id="foliage-bottom" x1="0" y1="0" x2="1" y2="0">
          <stop offset="0" stop-color="#c49a6c"/>
          <stop offset="0.55" stop-color="#c49a6c"/>
          <stop offset="0.78" stop-color="#5a2d1b"/>
          <stop offset="1" stop-color="#5a2d1b"/>
        </linearGradient>
      </defs>
      <path d="M0 234 V60 Q0 0 80 0 H340 V234 Z" fill="url(#foliage-bottom)" opacity="0.9"/>
    </svg>

    <span class="brand__dot"></span>
    <h1 class="brand__name">Marigolds</h1>
    <span class="brand__sub">Bakehouse</span>

    <p class="about">
      Marigolds Bakehouse is a wholesaler of gourmet brownies,<br>
      fudge and cookies to cafes, restaurants, hamper companies,<br>
      caterers, fine food stores and specialist chocolate shops.<br>
      All products are made with the finest ingredients - so why<br>
      not try Marigolds Bakehouse today to see why they are<br>
      “once tasted...never forgotten”.
    </p>

    <p class="contact">Email: marigoldsbakehouse@mailbrook.net</p>

    <p class="imprint">
      Produced by Marigolds Bakehouse, 48 Kellow St, Cheltenham VIC 3274<br>
      Ph: 047658913 · Email: marigoldsbakehouse@mailbrook.net
    </p>

    <h2 class="ingredients">Ingredients:</h2>

    <div class="barcode-area">
      <span class="barcode-area__label">BARCODE</span>
    </div>
  </main>
</body>
</html>
```